Business Cards

I'd like help creating business cards with the full logo "Velmora Capital Partners" on the back of the card (navy background with white writing), and abbreviated logo "VCP" on the front. Would like to list name, title, phone number, email, and website listed on front of card. Would like to keep very simple. Front font Arial or similar.

```html
<!DOCTYPE html>
<html lang="en">
<head>
<meta charset="UTF-8">
<title>Velmora Capital Partners – Business Cards</title>
<link href="https://fonts.googleapis.com/css2?family=Poppins:wght@400;500;700&display=swap" rel="stylesheet">
<style>
  :root {
    --navy: #1e3a6e;
    --white: #ffffff;
    --backdrop: #e9e6e1;
    --card-shadow: rgba(20, 30, 50, 0.25);
  }
  * { box-sizing: border-box; margin: 0; padding: 0; }
  html, body {
    width: 1200px; height: 900px; overflow: hidden;
    background: var(--backdrop);
    font-family: "Poppins", Arial, sans-serif;
  }
  .sheet {
    width: 1200px; height: 900px;
    display: flex; align-items: center; justify-content: center; gap: 40px;
  }
  .card {
    position: relative;
    width: 540px; height: 310px;
    box-shadow: 0 8px 22px var(--card-shadow);
    overflow: hidden;
  }
  /* Back */
  .card-back {
    background: var(--navy);
    display: flex; flex-direction: column; align-items: center; justify-content: center;
    color: var(--white);
  }
  .brand-name {
    font-weight: 700; font-size: 44px; letter-spacing: 4px; line-height: 1;
  }
  .brand-sub {
    font-weight: 700; font-size: 17px; letter-spacing: 9px; margin-top: 12px;
  }
  /* Front */
  .card-front { background: var(--white); color: var(--navy); }
  .wave { position: absolute; inset: 0; width: 100%; height: 100%; }
  .person { position: absolute; left: 38px; top: 62px; }
  .person-name { font-weight: 700; font-size: 22px; letter-spacing: 0.5px; line-height: 1.1; }
  .person-title { font-weight: 400; font-size: 15px; }
  .brand-short {
    position: absolute; right: 44px; top: 40px;
    font-weight: 700; font-size: 64px; line-height: 1; letter-spacing: 2px;
  }
  .contacts { position: absolute; left: 38px; top: 160px; list-style: none; }
  .contacts li { display: flex; align-items: center; gap: 10px; font-size: 15px; line-height: 1.6; }
  .contacts svg { width: 16px; height: 16px; fill: var(--navy); flex: none; }
  .website {
    position: absolute; right: 30px; bottom: 36px;
    color: var(--white); font-size: 14px;
  }
</style>
</head>
<body>
<main class="sheet">
  <section class="card card-back">
    <div class="brand-name">VELMORA</div>
    <div class="brand-sub">CAPITAL PARTNERS</div>
  </section>

  <section class="card card-front">
    <svg class="wave" viewBox="0 0 540 310" preserveAspectRatio="none" aria-hidden="true">
      <path d="M0 272 C160 272 270 248 350 208 C425 170 475 142 540 128 L540 310 L0 310 Z" fill="var(--navy)"/>
      <path d="M0 284 C165 284 280 258 362 214" fill="none" stroke="var(--white)" stroke-width="3"/>
    </svg>
    <div class="person">
      <div class="person-name">DANIEL HARTWELL</div>
      <div class="person-title">Managing Director</div>
    </div>
    <div class="brand-short">VCP</div>
    <ul class="contacts">
      <li>
        <svg viewBox="0 0 24 24"><path d="M6.6 10.8a15.1 15.1 0 0 0 6.6 6.6l2.2-2.2c.3-.3.7-.4 1-.2 1.1.4 2.3.6 3.6.6.6 0 1 .4 1 1V20c0 .6-.4 1-1 1C10.6 21 3 13.4 3 4c0-.6.4-1 1-1h3.5c.6 0 1 .4 1 1 0 1.3.2 2.5.6 3.6.1.3 0 .7-.2 1z"/></svg>
        044-987 654 321
      </li>
      <li>
        <svg viewBox="0 0 24 24"><path d="M2 5h20v14H2z M4 7v.3l8 5.4 8-5.4V7z" fill-rule="evenodd"/></svg>
        info@velmoracap.com
      </li>
    </ul>
    <div class="website">www.velmoracap.com</div>
  </section>
</main>
</body>
</html>
```